Business card for a new cabinet shop company named Marlowe Cabinets for high end cabinets

Design a business card, thinking dark rich green with colours to speak of high end luxury ie; cream, gold, black possibly

Peter Lindqvar
Director Craftsman
Email: info@marlowecabinets.com.au
Instagram : @marlowe.cabinets

```html
<!DOCTYPE html>
<html lang="en">
<head>
<meta charset="utf-8">
<title>Marlowe Cabinets — Business Card</title>
<link href="https://fonts.googleapis.com/css2?family=Lato:wght@400;700;900&display=swap" rel="stylesheet">
<style>
  :root {
    --backdrop: #26282b;
    --green: #0b4a2c;
    --green-deep: #073620;
    --gold: #d8b96f;
    --ink: #1c1c1c;
    --cream: #f6f1e4;
  }
  * { margin: 0; padding: 0; box-sizing: border-box; }
  html, body {
    width: 1200px; height: 900px; overflow: hidden;
    background: var(--backdrop);
    font-family: "Lato", sans-serif;
  }
  .sheet {
    width: 1200px; height: 900px;
    display: flex; flex-direction: column;
    align-items: center; justify-content: center; gap: 36px;
  }
  .card {
    position: relative;
    width: 720px; height: 412px;
    background: linear-gradient(135deg, var(--green) 0%, var(--green-deep) 100%);
    overflow: hidden;
    box-shadow: 0 10px 30px rgba(0,0,0,.45);
  }
  .card-art { position: absolute; inset: 0; }

  /* Front */
  .front-brand {
    position: absolute; inset: 0;
    display: flex; align-items: center; justify-content: center; gap: 18px;
  }
  .brand-square { width: 34px; height: 34px; background: var(--gold); }
  .front-brand .brand-name {
    font-size: 50px; font-weight: 700; color: var(--gold); letter-spacing: 1px;
  }

  /* Back */
  .back-brand {
    position: absolute; left: 44px; top: 150px;
    display: flex; align-items: center; gap: 10px;
  }
  .back-brand .brand-square { width: 16px; height: 16px; }
  .back-brand .brand-name {
    font-size: 22px; font-weight: 700; color: var(--gold);
  }
  .holder-name {
    position: absolute; right: 30px; top: 22px;
    font-size: 32px; font-weight: 900; color: var(--ink);
    text-transform: uppercase; letter-spacing: .5px;
  }
  .holder-role {
    position: absolute; left: 26px; bottom: 24px;
    font-size: 27px; font-weight: 900; color: var(--ink);
    text-transform: uppercase;
  }
  .contact-list {
    position: absolute; left: 300px; top: 150px;
    list-style: none; display: flex; flex-direction: column; gap: 22px;
  }
  .contact-item {
    display: flex; align-items: center; gap: 16px;
    font-size: 21px; color: var(--cream);
  }
  .contact-icon {
    width: 34px; height: 34px; background: var(--gold);
    display: flex; align-items: center; justify-content: center;
  }
</style>
</head>
<body>
<main class="sheet">

  <section class="card card-front" aria-label="Card front">
    <div class="front-brand">
      <span class="brand-square"></span>
      <span class="brand-name">Marlowe Cabinets</span>
    </div>
  </section>

  <section class="card card-back" aria-label="Card back">
    <svg class="card-art" viewBox="0 0 720 412" aria-hidden="true">
      <polygon points="340,0 720,0 720,88 366,88" fill="var(--gold)"/>
      <polygon points="0,328 400,328 370,412 0,412" fill="var(--gold)"/>
      <rect x="36" y="54" width="270" height="4" fill="var(--gold)"/>
      <rect x="420" y="314" width="270" height="4" fill="var(--gold)"/>
    </svg>

    <div class="back-brand">
      <span class="brand-square"></span>
      <span class="brand-name">Marlowe Cabinets</span>
    </div>

    <h1 class="holder-name">Peter Lindqvar</h1>

    <ul class="contact-list">
      <li class="contact-item">
        <span class="contact-icon">
          <svg width="20" height="14" viewBox="0 0 20 14" aria-hidden="true">
            <rect x="1" y="1" width="18" height="12" fill="none" stroke="var(--green)" stroke-width="2"/>
            <polyline points="1,1 10,8 19,1" fill="none" stroke="var(--green)" stroke-width="2"/>
          </svg>
        </span>
        info@marlowecabinets.com.au
      </li>
      <li class="contact-item">
        <span class="contact-icon"></span>
        @marlowe.cabinets
      </li>
    </ul>

    <p class="holder-role">Director Craftsman</p>
  </section>

</main>
</body>
</html>
```